Texas Based IT Company Needs a Brochure Design

We need a trifold brochure design for our new IT company, Marlow Tech Services, based in New Braunfels, TX. This brochure will be for marketing to our residential as well as our business customers. We would like the plans & subscriptions shown below displayed on the brochure. We also would like a brief description of our family owned company. I would also like our company mission statement displayed on the brochure (mission statement provided below). I would also like to make it known to the customer that every plan is customizable and can fit their individual needs as well as provide priority support servicing. Please see marlowtechsvc.example for a more thorough description of services provided and description of company. I would also like the brochure to match the design/color scheme of the website, however this is not a must have, I want the designers to have a free choice of color/design.
Company description:
We will offer subscription based support services to help our customers better plan & manage IT expenses. Customers who purchase these packages will be given priority support as well as the ability to roll over hours purchased month to month. This will help offset the cost of large scale emergencies or when business threatening disasters happen. We will also offer discounted hourly rates, based on the package selected, for any hours in excess of the subscription.
We will offer support & Infrastructure subscription services to help our customers not have to foot the bill up front for enterprise level IT devices & hardware. This will also provide support & maintenance for our customers that purchase these products & services. We will offer packages specifically tailored to our clients needs. We will not have cookie cutter based subscription & infrastructure packages.
Company mission statement:
Assist our team members and fellow coworkers grow in their role. Facilitate a family oriented work place and family type culture in our company. To provide our employees an environment were they can grow in both knowledge and skills needed to be successful in their roles. To help our customers increase productivity and more effectively manage costs associated with IT expenditures. Add value to our customers businesses by offering Win-Win solutions to help facilitate success and company growth. To only implement products and services that perfectly fit our clients needs. We will always execute our business honestly, ethically, and with the highest level of integrity.
Here is a brief description of our service packages and equipment lease options:
$70 per hour regular residential rate (without subscription)
$125 per hour regular business rate (without subscription)
Business Support Subscription:
1 hour business package - $ 99 monthly - 10% discount on regular hourly rate after overage
2 hour business package - $149 monthly - 15% discount on regular hourly rate after overage
3 hour business package - $199 monthly - 20% discount on regular hourly rate after overage
Custom plans to meet client needs available
Residential Support Subscription:
1 hour residential package - $59 monthly - 10% discount on regular hourly rate after overage
2 hour residential package - $79 monthly - 15% discount on regular hourly rate after overage
3 hour residential package - $99 monthly - 20% discount on regular hourly rate after overage
Equipment lease (hardware support only) - Client purchases equipment for $1 at end of term (Storage devices, Servers, Software Licenses, etc.):
1 year lease - 12 total payments made (Rate based on credit worthiness)
2 year lease - 24 total payments made (Rate based on credit worthiness)
Custom plans/rates that provide a win/win solution
Equipment lease (Hardware support included) + Service Subscription
*Normal lease prices with discounted service subscription shown below:
1 hour business package - $ 79 monthly - 15% discount on regular hourly rate after overage
2 hour business package - $129 monthly - 20% discount on regular hourly rate after overage
3 hour business package - $179 monthly - 25% discount on regular hourly rate after overage
custom plans to meet client needs available
Updates
I am afraid we have changed the information provided earlier in the brief. I am very sorry about this. Here is an update to our services/subscription based plans. This brochure will not be geared to both business and residential clients:$70 per hour regular residential rate (without subscription)$125 per hour regular business rate (without subscription)Business Support Subscription:1 hour business package - $ 99 monthly - 10% discount on regular hourly rate after overage2 hour business package - $149 monthly - 15% discount on regular hourly rate after overage3 hour business package - $199 monthly - 20% discount on regular hourly rate after overageCustom plans to meet client needs availableResidential Support Subscription:1 hour residential package - $59 monthly - 10% discount on regular hourly rate after overage2 hour residential package - $79 monthly - 15% discount on regular hourly rate after overage3 hour residential package - $99 monthly - 20% discount on regular hourly rate after overageCustom plans to meet client needs availableEquipment lease (hardware support only) - Client purchases equipment for $1 at end of term (Storage devices, Servers, Software Licenses, etc.):1 year lease - 12 total payments made (Rate based on credit worthiness)2 year lease - 24 total payments made (Rate based on credit worthiness)Custom plans/rates that provide a win/win solutionEquipment lease (Hardware support included) + Service Subscription*Normal lease prices with discounted service subscription shown below:1 hour business package - $ 79 monthly - 15% discount on regular hourly rate after overage2 hour business package - $129 monthly - 20% discount on regular hourly rate after overage3 hour business package - $179 monthly - 25% discount on regular hourly rate after overagecustom plans to meet client needs available Added Wednesday, September 23, 2015
Target Market(s)
Residential Clients
Industry/Entity Type
Information Technology
Look and feel

```html
<!DOCTYPE html>
<html lang="en">
<head>
<meta charset="utf-8">
<title>Marlow Tech Services – Brochure</title>
<link rel="stylesheet" href="https://fonts.googleapis.com/css2?family=Oswald:wght@300;400;500&family=Open+Sans:wght@400;600;700&display=swap">
<style>
:root{
  --page:#e4e5e7;
  --navy:#0d1a33;
  --navy-2:#15254a;
  --blue:#1f5fc8;
  --blue-light:#3f8cf0;
  --blue-dark:#123d8c;
  --orange:#f2a43a;
  --orange-dark:#d67f14;
  --grey-box:#3a4358;
  --grey-light:#c9ccd3;
  --white:#ffffff;
  --ink:#1b2a4a;
}
*{box-sizing:border-box;margin:0;padding:0}
html,body{width:783px;height:1200px;overflow:hidden}
body{background:var(--page);position:relative;font-family:"Open Sans",Arial,sans-serif;color:var(--white)}

/* ---------- cover panel ---------- */
.cover{position:absolute;left:262px;top:28px;width:260px;height:580px;background:var(--white);box-shadow:0 4px 14px rgba(0,0,0,.18);overflow:hidden}
.brand{text-align:center;padding-top:18px;color:var(--ink);font-family:"Oswald",Arial,sans-serif;font-weight:400;line-height:1}
.brand-name{font-size:34px;letter-spacing:1px}
.brand-sub{font-size:14px;letter-spacing:9px;margin-top:4px}
.devices{position:absolute;left:20px;top:102px;width:220px;height:150px;background:radial-gradient(ellipse at center,#cfd6e2 0%,#eef1f6 70%,#fff 100%)}
.cover-heading{position:absolute;top:264px;width:100%;text-align:center;color:var(--ink);font-family:"Oswald",Arial,sans-serif;font-size:20px;letter-spacing:.5px}
.rates{position:absolute;top:296px;width:100%;display:flex;justify-content:space-around;padding:0 16px}
.rate{text-align:center;color:var(--blue)}
.rate-price{font-size:22px;font-weight:600;font-family:"Oswald",Arial,sans-serif}
.rate-price sup{font-size:12px}
.rate-price small{font-size:13px}
.rate-note{font-size:8px;color:var(--ink);font-style:italic}
.cover-stripe{position:absolute;top:360px;left:0;width:100%;height:7px;background:var(--blue)}
.tech-scene{position:absolute;top:367px;left:0;width:100%;height:195px;background:radial-gradient(ellipse at 55% 45%,#2f8fb0 0%,#123a5a 40%,#07142a 85%)}
.cover-band{position:absolute;bottom:0;left:0;width:100%;height:18px;background:var(--blue)}

/* ---------- inside spread ---------- */
.spread{position:absolute;left:47px;top:640px;width:689px;height:520px;background:linear-gradient(180deg,var(--navy-2),var(--navy));box-shadow:0 4px 14px rgba(0,0,0,.22);overflow:hidden}
.spread-title{height:60px;background:linear-gradient(90deg,var(--blue-dark),var(--blue) 55%,var(--blue-light));display:flex;align-items:flex-end;justify-content:space-between;padding:0 26px 8px;font-family:"Oswald",Arial,sans-serif;font-weight:300;font-size:33px;letter-spacing:2px}
.columns{display:grid;grid-template-columns:repeat(3,1fr);gap:18px;padding:14px 24px 0}
.col-head{height:42px;background:var(--grey-light);color:var(--ink);font-size:11.5px;line-height:1.25;display:flex;align-items:center;justify-content:center;text-align:center;padding:0 8px}
.col-head.residential{background:var(--orange)}
.col-head.lease{background:#aeb3bd}
.tab{margin:12px auto 0;width:130px;height:20px;background:var(--blue);font-size:11px;font-weight:600;text-align:center;line-height:20px;clip-path:polygon(8% 0,92% 0,100% 100%,0 100%)}
.tab-note{font-size:6.5px;text-align:center;color:#aeb8cc;margin:4px 0 6px}
.plan{display:flex;height:52px;margin-bottom:8px;background:var(--grey-box)}
.plan-price{flex:1;display:flex;align-items:center;gap:6px;padding-left:8px;background:linear-gradient(180deg,var(--blue-light),var(--blue-dark))}
.residential-col .plan-price{background:linear-gradient(180deg,var(--orange),var(--orange-dark))}
.amount{font-size:27px;font-weight:400;font-family:"Oswald",Arial,sans-serif}
.amount sup{font-size:13px;vertical-align:12px}
.hours{font-size:10px;font-weight:700;line-height:1.15}
.discount{width:48px;display:flex;flex-direction:column;align-items:center;justify-content:center;background:var(--blue);font-size:14px;font-weight:700;line-height:1}
.discount span{font-size:7px;font-weight:400;margin-top:2px}
.custom-band{margin:6px 0 0;height:26px;background:linear-gradient(90deg,var(--blue-dark),var(--blue),var(--blue-dark));font-family:"Oswald",Arial,sans-serif;font-weight:300;font-size:17px;letter-spacing:3px;text-align:center;line-height:26px}
.lease-row{display:grid;grid-template-columns:190px 1fr 1fr 110px;gap:10px;padding:12px 24px 0}
.lease-box{height:82px;background:#7c8394;padding:8px 10px;font-size:8px;line-height:1.3}
.lease-box.main{background:var(--grey-light);color:var(--ink)}
.lease-box h3{font-size:17px;font-weight:700;margin-bottom:3px}
.lease-box .term{font-size:13px;font-weight:600;text-align:center;margin-top:4px}
.lease-box .count{font-size:11px;text-align:center}
.lease-box .fine{font-size:7px;text-align:center;margin-top:10px;color:#e0e4ea}
.lease-box.custom{background:var(--grey-box);font-size:8.5px;display:flex;align-items:center}
.lease-box .highlight{font-size:10px;font-weight:700;color:var(--blue)}
</style>
</head>
<body>

<section class="cover">
  <div class="brand">
    <div class="brand-name">MARLOW TECH</div>
    <div class="brand-sub">SERVICES</div>
  </div>
  <div class="devices" role="img" aria-label="Photo of laptops, tablets, phones and a router"></div>
  <h2 class="cover-heading">RESIDENTIAL SOLUTIONS</h2>
  <div class="rates">
    <div class="rate"><div class="rate-price"><sup>$</sup>70<small>/hour</small></div><div class="rate-note">regular residential rate</div></div>
    <div class="rate"><div class="rate-price"><sup>$</sup>125<small>/hour</small></div><div class="rate-note">regular business rate</div></div>
  </div>
  <div class="cover-stripe"></div>
  <div class="tech-scene" role="img" aria-label="Blue digital technology scene with glowing circuitry"></div>
  <div class="cover-band"></div>
</section>

<section class="spread">
  <header class="spread-title"><span>HIGH END</span><span>SUBSCRIPTION</span><span>PACKAGES</span></header>

  <div class="columns">
    <div class="business-col">
      <div class="col-head">Business Support<br>Subscription:</div>
      <div class="tab">Business Package</div>
      <div class="tab-note">Discount on regular hourly rate after overage</div>
      <div class="plan"><div class="plan-price"><span class="amount"><sup>$</sup>99</span><span class="hours">1 HOUR<br>MONTHLY</span></div><div class="discount">10%<span>discount</span></div></div>
      <div class="plan"><div class="plan-price"><span class="amount"><sup>$</sup>149</span><span class="hours">2 HOUR<br>MONTHLY</span></div><div class="discount">15%<span>discount</span></div></div>
      <div class="plan"><div class="plan-price"><span class="amount"><sup>$</sup>199</span><span class="hours">3 HOUR<br>MONTHLY</span></div><div class="discount">20%<span>discount</span></div></div>
    </div>
    <div class="residential-col">
      <div class="col-head residential">Residential Support<br>Subscription:</div>
      <div class="tab">Residential Package</div>
      <div class="tab-note">Discount on regular hourly rate after overage</div>
      <div class="plan"><div class="plan-price"><span class="amount"><sup>$</sup>59</span><span class="hours">1 HOUR<br>MONTHLY</span></div><div class="discount">10%<span>discount</span></div></div>
      <div class="plan"><div class="plan-price"><span class="amount"><sup>$</sup>79</span><span class="hours">2 HOUR<br>MONTHLY</span></div><div class="discount">15%<span>discount</span></div></div>
      <div class="plan"><div class="plan-price"><span class="amount"><sup>$</sup>99</span><span class="hours">3 HOUR<br>MONTHLY</span></div><div class="discount">20%<span>discount</span></div></div>
    </div>
    <div class="lease-col">
      <div class="col-head lease">Equipment lease +<br>Service Subscription</div>
      <div class="tab">Business Package</div>
      <div class="tab-note">Normal lease prices with discounted subscription</div>
      <div class="plan"><div class="plan-price"><span class="amount"><sup>$</sup>79</span><span class="hours">1 HOUR<br>MONTHLY</span></div><div class="discount">15%<span>discount</span></div></div>
      <div class="plan"><div class="plan-price"><span class="amount"><sup>$</sup>129</span><span class="hours">2 HOUR<br>MONTHLY</span></div><div class="discount">20%<span>discount</span></div></div>
      <div class="plan"><div class="plan-price"><span class="amount"><sup>$</sup>179</span><span class="hours">3 HOUR<br>MONTHLY</span></div><div class="discount">25%<span>discount</span></div></div>
    </div>
  </div>

  <div class="custom-band">CUSTOM PLANS TO MEET CLIENT NEEDS AVAILABLE</div>

  <div class="lease-row">
    <div class="lease-box main">
      <h3>Equipment lease</h3>
      <div>Hardware support only</div>
      <div class="highlight">$1 at end of term</div>
      <div>Storage devices, servers, licenses</div>
    </div>
    <div class="lease-box">
      <div class="term">1 year lease</div>
      <div class="count">12 total payments made</div>
      <div class="fine">Rate based on credit worthiness</div>
    </div>
    <div class="lease-box">
      <div class="term">2 year lease</div>
      <div class="count">24 total payments made</div>
      <div class="fine">Rate based on credit worthiness</div>
    </div>
    <div class="lease-box custom">Custom plans.<br>Rates that provide a win/win solution</div>
  </div>
</section>

</body>
</html>
```